PREMIUM AGENCY High End Business Card - A+++ Designers Wanted

** DO NOT ATTEMPT TO CONTACT ME THROUGH SEARCHING ON ZINTREL OR EMAILING ME THROUGH MY WEBSITE **

I need a fresh, contemporary business card designed using the logo attached (BRONSALK)

I have attached the font for BRONSALK

It must have a premium look and feel. The business card size must be STANDARD size.

You can submit either/both VERTICAL or HORIZONTAL designs.

FRONT: It must have the following sample information on

Paul Ardley
Director Operations
Mobile +61 452 118 906
Email paulardley@bronsalk.com
www.bronsalk.com

The REAR of the business card must have the words

BUILD IMAGINE FORWARD

as part of the design, in the same font (NEXA) attached.

The words do not need to be in capitals, or on the same line, please design this as you see it best working.

ADDITIONAL INFORMATION
======================

The BRONSALK logo must be on the front of the card

I want Ultraviolet printing on the final design, to enhance either the NAME of the person OR the BRONSALK logo OR the words on the back of the card.

Target Market(s)

Agency, Advertising Agency, Creative, Designers

Industry/Entity Type

Media

Contact Information for Business Card

Design Agency, Contemporary, Premium look and feel, High Quality

Font styles to use
Serif
Sans Serif
Other font styles liked:
• ATTACHED TO PROJECT

Requirements
Must have
• BLACK & WHITE as the primary design, and if you feel there can be a highlighted colour, then this can be used.
• The Logo ICON attached is blue, this colour must not be changed.
• I have attached the partner brand BRONSALK MEDIA incase you need to manipulate the original files.
• ** DO NOT ATTEMPT TO CONTACT ME THROUGH SEARCHING ON ZINTREL OR EMAILING ME THROUGH MY WEBSITE **
Nice to have
• Must be Premium. I have attached some sample designs, that I like that would be a good inspiration for where this can be taken.
• My favourite design is is the KESTRAVUE2-BUSINESSCARD-TEMPLATE
Should not have
• No funny or silly standard / off the shelf designs

```html
<!DOCTYPE html>
<html lang="en">
<head>
<meta charset="utf-8">
<title>Bronsalk Business Card</title>
<link rel="stylesheet" href="https://fonts.googleapis.com/css2?family=Montserrat:wght@400;500;600;700&display=swap">
<style>
  :root {
    --navy-deep: #161b26;
    --navy-mid: #2b323e;
    --navy-light: #474f5c;
    --accent-blue: #1cc3f2;
    --paper-light: #f1f1f1;
    --paper-grey: #d9dadc;
    --ink-black: #15181d;
    --text-white: #ffffff;
    --page-bg: #e6e6e8;
  }
  * { box-sizing: border-box; margin: 0; padding: 0; }
  html, body {
    width: 1200px; height: 1000px; overflow: hidden;
    background: var(--page-bg);
    font-family: "Montserrat", sans-serif;
  }
  .stage {
    position: relative; width: 1200px; height: 1000px;
    display: flex; justify-content: center; align-items: center; gap: 60px;
  }
  .card {
    position: relative; width: 360px; height: 630px;
    border: 5px solid var(--accent-blue);
    border-radius: 4px; overflow: hidden;
    background: linear-gradient(160deg, var(--navy-deep) 0%, var(--navy-mid) 55%, var(--navy-light) 75%, var(--navy-deep) 100%);
    box-shadow: 0 12px 30px rgba(0,0,0,0.25);
  }

  /* Back side */
  .brand {
    position: absolute; display: flex; align-items: center; gap: 12px;
    font-weight: 600; letter-spacing: 0.14em; white-space: nowrap;
  }
  .brand-dot {
    width: 16px; height: 16px; border-radius: 50%;
    background: var(--accent-blue);
  }
  .card-back .brand {
    top: 255px; left: 0; right: 0; justify-content: center;
    font-size: 34px; color: var(--text-white);
  }
  .tagline-tab {
    position: absolute; left: 0; bottom: 0;
    width: 255px; height: 48px;
    background: var(--accent-blue);
    border-top-right-radius: 22px;
    display: flex; align-items: center; padding-left: 16px;
    color: var(--text-white); font-size: 12px; font-weight: 600; letter-spacing: 0.04em;
    white-space: nowrap;
  }

  /* Front side */
  .front-header {
    position: absolute; top: 0; left: 0; right: 0; height: 195px;
    background: linear-gradient(180deg, var(--paper-light), var(--paper-grey));
  }
  .header-tab {
    position: absolute; top: 0; right: 0; width: 190px; height: 32px;
    background: var(--accent-blue);
    border-bottom-left-radius: 22px;
  }
  .card-front .brand {
    top: 95px; left: 30px;
    font-size: 32px; color: var(--ink-black);
  }
  .person-name {
    position: absolute; top: 215px; left: 110px; color: var(--accent-blue); font-weight: 600; line-height: 1;
  }
  .person-first { font-size: 62px; display: block; }
  .person-last { font-size: 32px; display: block; margin-top: -2px; }
  .person-role {
    display: block; margin-top: 6px;
    color: var(--text-white); font-size: 15px; font-weight: 600;
  }
  .contact-tab {
    position: absolute; left: 0; top: 335px; width: 56px; height: 240px;
    background: var(--accent-blue);
    border-top-right-radius: 22px; border-bottom-right-radius: 22px;
    display: flex; flex-direction: column; align-items: center; justify-content: center; gap: 30px;
  }
  .contact-tab svg { width: 16px; height: 16px; }
  .contact-list {
    position: absolute; left: 110px; top: 395px; list-style: none;
    color: var(--text-white); font-size: 15px; font-weight: 500; white-space: nowrap;
  }
  .contact-list li { margin-bottom: 30px; }
</style>
</head>
<body>
<main class="stage">
  <section class="card card-back" aria-label="Card back">
    <div class="brand"><span class="brand-dot"></span><span>BRONSALK</span></div>
    <div class="tagline-tab">BUILD IMAGINE FORWARD</div>
  </section>

  <section class="card card-front" aria-label="Card front">
    <div class="front-header"><div class="header-tab"></div></div>
    <div class="brand"><span class="brand-dot"></span><span>BRONSALK</span></div>
    <div class="person-name">
      <span class="person-first">Paul</span>
      <span class="person-last">Ardley</span>
      <span class="person-role">Director Operations</span>
    </div>
    <div class="contact-tab">
      <svg viewBox="0 0 24 24" aria-hidden="true"><path fill="#fff" d="M6.6 10.8a15.1 15.1 0 0 0 6.6 6.6l2.2-2.2a1 1 0 0 1 1-.25 11.4 11.4 0 0 0 3.6.57 1 1 0 0 1 1 1V20a1 1 0 0 1-1 1A17 17 0 0 1 3 4a1 1 0 0 1 1-1h3.5a1 1 0 0 1 1 1c0 1.250.2 2.45.57 3.6a1 1 0 0 1-.25 1z"/></svg>
      <svg viewBox="0 0 24 24" aria-hidden="true"><path fill="#fff" d="M2 11 22 3l-8 20-3-9z"/></svg>
      <svg viewBox="0 0 24 24" aria-hidden="true"><circle cx="12" cy="12" r="10" fill="none" stroke="#fff" stroke-width="2"/><path d="M2 12h20M12 2c3 3 3 17 0 20M12 2c-3 3-3 17 0 20" fill="none" stroke="#fff" stroke-width="1.6"/></svg>
    </div>
    <ul class="contact-list">
      <li>+61 452 118 906</li>
      <li>paulardley@bronsalk.com</li>
      <li>www.bronsalk.com</li>
    </ul>
  </section>
</main>
</body>
</html>
```